Crestwell Advisory Services

I'm looking to create a flyer for my business to provide a consultant service. I will be providing the following below
Launch Your Business Today for only $150
(state fee not included)
Business Formation includes:
*Limited liability Corporation (LLC)
*Halvers and Quint Number
*FEIN
*Operation Agreement for partnership LLCs (For 2 or more member(s)
*Commercial Activity license (If needed for your Business )
*Same -day turnaround service with documents
Schedule your Appointment today
Call or text:318-472-6051
Email:MoralesCapitalCircle@fernmail.net
Target Market(s)
I want the flyer to attract people who wants to start a business but doesn’t know where to start. I want the flyer to stand out form the other consultant businesses.
Industry/Entity Type
Consultant
Requirements
Must have
- The State fee not included should be in small print
Highlight the price or service
Highlight the phrase "launch you business today"
Nice to have
- Different samples of colors, a variety
Should not have
- should not be all one color

```html
<!DOCTYPE html>
<html lang="en">
<head>
<meta charset="utf-8">
<title>Crestwell Advisory Services – Business Formation Flyer</title>
<link rel="stylesheet" href="https://fonts.googleapis.com/css2?family=Gelasio:wght@400;700&family=Roboto+Condensed:wght@700&family=Lato:wght@400;700&display=swap">
<style>
  :root {
    --ink: #0b0b0d;
    --paper: #ffffff;
    --blue-deep: #0f2f7a;
    --blue-mid: #1d4fb0;
    --blue-light: #4f86d6;
    --frame-orange: #f26a1b;
    --band-red: #ea3349;
    --band-orange: #e2611a;
    --band-orange-dark: #c94e10;
    --tick-blue: #1f4fa0;
    --tick-orange: #f26a1b;
    --text-dark: #1a1a1a;
    --divider: #b9bcc4;
  }
  * { box-sizing: border-box; margin: 0; padding: 0; }
  html, body {
    width: 900px; height: 1200px; overflow: hidden;
    background: var(--paper);
  }
  .flyer {
    position: relative; width: 900px; height: 1200px;
    background: var(--paper);
    font-family: "Gelasio", Georgia, serif;
    overflow: hidden;
  }
  .contact-bar {
    position: absolute; left: 0; top: 59px; width: 900px; height: 44px;
    background: var(--ink);
    display: flex; align-items: center; justify-content: flex-end;
    padding-right: 33px; gap: 9px;
    color: var(--paper);
    font-family: "Lato", Arial, sans-serif; font-size: 13.5px; letter-spacing: 0.3px;
    text-transform: uppercase;
  }
  .hero-visual {
    position: absolute; left: 0; top: 103px; width: 900px; height: 443px;
    background:
      radial-gradient(ellipse at 72% 40%, rgba(120,170,240,0.55), transparent 55%),
      radial-gradient(ellipse at 90% 75%, rgba(90,140,220,0.4), transparent 50%),
      linear-gradient(120deg, var(--blue-deep) 0%, var(--blue-mid) 45%, var(--blue-light) 75%, var(--blue-mid) 100%);
  }
  .headline-frame {
    position: absolute; left: 39px; top: 38px; width: 427px; height: 475px;
    border: 5px solid var(--frame-orange); border-radius: 3px;
    color: var(--paper); text-align: center;
  }
  .headline-frame .launch {
    position: absolute; left: 0; right: 0; top: 90px;
    font-size: 54px; line-height: 60px; font-weight: 400; letter-spacing: 1px;
  }
  .headline-frame .business {
    position: absolute; left: 0; right: 0; top: 213px;
    font-size: 60px; line-height: 60px; font-weight: 700; letter-spacing: 1px;
  }
  .headline-frame .today {
    position: absolute; left: 0; right: 0; top: 276px;
    font-size: 33px; line-height: 36px; font-weight: 700; letter-spacing: 0.5px;
  }
  .headline-frame .price-line {
    position: absolute; left: 0; right: 0; top: 308px;
    font-size: 38px; line-height: 70px;
  }
  .headline-frame .price {
    font-family: "Roboto Condensed", Arial, sans-serif; font-weight: 700; font-size: 60px;
  }
  .headline-frame .fine-print {
    position: absolute; left: 0; right: 0; top: 406px;
    font-size: 21px; font-weight: 700;
  }
  .includes-band {
    position: absolute; left: 0; top: 562px; width: 900px; height: 76px;
    background: var(--band-red);
    display: flex; align-items: center; justify-content: center;
    font-size: 40px; font-weight: 700; color: var(--paper); letter-spacing: 0.3px;
  }
  .includes-band .accent { color: var(--ink); margin-left: 12px; }
  .features {
    position: absolute; left: 0; top: 638px; width: 900px; height: 206px;
    background: linear-gradient(90deg, #e7e9ee 0%, #f7f7f9 40%, #ffffff 70%, #eeeff2 100%);
  }
  .features .divider {
    position: absolute; left: 447px; top: 14px; width: 1px; height: 178px;
    background: var(--divider);
  }
  .feature {
    position: absolute; display: flex; align-items: flex-start; gap: 18px;
    font-size: 26px; line-height: 31px; color: var(--text-dark);
  }
  .feature svg { flex: none; }
  .service-band {
    position: absolute; left: 0; top: 855px; width: 900px; height: 152px;
    background: linear-gradient(90deg, var(--band-orange-dark) 0%, var(--band-orange) 50%, #ea6d23 100%);
  }
  .service {
    position: absolute; left: 78px; display: flex; align-items: center; gap: 14px;
    font-size: 26px; color: var(--paper);
  }
  .footer {
    position: absolute; left: 0; top: 1018px; width: 900px; height: 182px;
    background: var(--ink); color: var(--paper); text-align: center;
  }
  .footer .schedule { position: absolute; left: 0; right: 0; top: 34px; font-size: 27px; }
  .footer .call {
    position: absolute; left: 0; right: 0; top: 78px; font-size: 42px; letter-spacing: 0.5px;
  }
  .footer .call .number {
    font-family: "Roboto Condensed", Arial, sans-serif; font-weight: 700; font-size: 44px;
  }
</style>
</head>
<body>
<main class="flyer">
  <div class="hero-visual" role="img" aria-label="Blue consulting concept photo with hand touching hexagon business icons"></div>

  <header class="contact-bar">
    <svg width="18" height="13" viewBox="0 0 18 13" aria-hidden="true">
      <rect x="0.75" y="0.75" width="16.5" height="11.5" fill="none" stroke="#fff" stroke-width="1.5"/>
      <polyline points="1,1 9,7.5 17,1" fill="none" stroke="#fff" stroke-width="1.5"/>
    </svg>
    <span>MoralesCapitalCircle@fernmail.net</span>
  </header>

  <section class="headline-frame">
    <p class="launch">LAUNCH<br>YOUR</p>
    <p class="business">BUSINESS</p>
    <p class="today">TODAY FOR</p>
    <p class="price-line">ONLY <span class="price">$150</span></p>
    <p class="fine-print">(state fee not included)</p>
  </section>

  <h2 class="includes-band">BUSINESS FORMATION<span class="accent">INCLUDES</span></h2>

  <section class="features">
    <div class="divider"></div>
    <div class="feature" style="left:60px; top:30px;">
      <svg width="52" height="52" viewBox="0 0 52 52" aria-hidden="true"><circle cx="24" cy="28" r="19" fill="none" stroke="var(--tick-blue)" stroke-width="2.5"/><path d="M13 27 L22 37 L42 8" fill="none" stroke="var(--tick-orange)" stroke-width="5" stroke-linecap="round" stroke-linejoin="round"/></svg>
      <span>Limited liability<br>Corporation (LLC)</span>
    </div>
    <div class="feature" style="left:60px; top:120px;">
      <svg width="52" height="52" viewBox="0 0 52 52" aria-hidden="true"><circle cx="24" cy="28" r="19" fill="none" stroke="var(--tick-blue)" stroke-width="2.5"/><path d="M13 27 L22 37 L42 8" fill="none" stroke="var(--tick-orange)" stroke-width="5" stroke-linecap="round" stroke-linejoin="round"/></svg>
      <span>Halvers and Quint<br>Number</span>
    </div>
    <div class="feature" style="left:488px; top:22px;">
      <svg width="52" height="52" viewBox="0 0 52 52" aria-hidden="true"><circle cx="24" cy="28" r="19" fill="none" stroke="var(--tick-blue)" stroke-width="2.5"/><path d="M13 27 L22 37 L42 8" fill="none" stroke="var(--tick-orange)" stroke-width="5" stroke-linecap="round" stroke-linejoin="round"/></svg>
      <span>FEIN</span>
    </div>
    <div class="feature" style="left:488px; top:104px;">
      <svg width="52" height="52" viewBox="0 0 52 52" aria-hidden="true"><circle cx="24" cy="28" r="19" fill="none" stroke="var(--tick-blue)" stroke-width="2.5"/><path d="M13 27 L22 37 L42 8" fill="none" stroke="var(--tick-orange)" stroke-width="5" stroke-linecap="round" stroke-linejoin="round"/></svg>
      <span>Operation Agreement for<br>partnership LLCs (For 2<br>or&nbsp; more member(s)</span>
    </div>
  </section>

  <section class="service-band">
    <div class="service" style="top:24px;">
      <svg width="48" height="48" viewBox="0 0 48 48" aria-hidden="true"><circle cx="22" cy="26" r="18" fill="none" stroke="#fff" stroke-width="2.5"/><path d="M11 25 L20 35 L40 6" fill="none" stroke="#fff" stroke-width="5" stroke-linecap="round" stroke-linejoin="round"/></svg>
      <span>Commercial Activity license (If needed for your Business )</span>
    </div>
    <div class="service" style="top:80px;">
      <svg width="48" height="48" viewBox="0 0 48 48" aria-hidden="true"><circle cx="22" cy="26" r="18" fill="none" stroke="#fff" stroke-width="2.5"/><path d="M11 25 L20 35 L40 6" fill="none" stroke="#fff" stroke-width="5" stroke-linecap="round" stroke-linejoin="round"/></svg>
      <span>Same -day turnaround service with documents</span>
    </div>
  </section>

  <footer class="footer">
    <p class="schedule">schedule your Appointment today</p>
    <p class="call">CALL OR TEXT:<span class="number">318-472-6051</span></p>
  </footer>
</main>
</body>
</html>
```